Lumivane company website, a website for employment for people with autism

The website will make a match between people and jobs, mainly in the graphical sector, but also other sectors.
The name of the company is lumivane and automates jobs with people that are on the autism spectrum.
The whole matchmaking and feedback process and so doesn't have to be in this prototype, we just want the general information pages and to convey a great look and brand identity that we will keep in the other pages to be developed. The website must be made with Wordpress, since the backend will be developed in Wordpress too.
It is a social project that wants to create possibilites for people with ASS to work from home for an employer or to do a variety of tasks for different customers.
The people we hire are generally not on the regular job market or have difficulty finding a job and "selling themselves"

Target Market(s)

matchmaking between talent (with ASS) and employers / jobs

Number of Pages Required

5+ page

Font styles to use
Sans Serif

Colors
ec1f27
e34298
a64599
6b449b
0355a3
0792cd

Requirements
Must have
• A stunning landing pages
• Integrate our logo and must match with what will do. We want a clean, modern, minimalistic, sleek website that radiates creativity and good looks.
• We have one page describing what we can do for customers, one page for people with ASS that would like to be candidates (our approach, learning program, ...), two pages that are addressed to partners who want to cooperate: the one's that can assist with autism related assistance and the one's that can help with the job coaching.
Nice to have
• In our logo are many colors as we embrace diversity and want to show that. Out main branding colors are red (for action) and blue for stability and will all gradients that go with it. Mainly white or black (or anthracite) for other parts
Should not have
• We want a modern and minimalistic design, no fluffy designs with lots of ornaments.

```html
<!DOCTYPE html>
<html lang="en">
<head>
<meta charset="utf-8">
<title>Lumivane — Employment for people on the autism spectrum</title>
<link href="https://fonts.googleapis.com/css2?family=Barlow:wght@400;500;600&family=Montserrat:wght@300;400;600;700&display=swap" rel="stylesheet">
<style>
:root{
  --red:#ec1f27;--pink:#e34298;--violet:#a64599;--purple:#6b449b;--blue:#0355a3;--sky:#0792cd;
  --navy:#1c3a7a;--ink:#222;--text:#444;--muted:#666;--grey:#ececec;--grey-2:#e4e4e4;--white:#fff;
}
*{box-sizing:border-box;margin:0;padding:0}
html,body{width:1200px;height:4138px;overflow:hidden;background:var(--white)}
body{position:relative;font-family:"Barlow",sans-serif;color:var(--text)}
.abs{position:absolute}
h2.section-title{font-family:"Montserrat",sans-serif;font-weight:300;font-size:38px;color:var(--ink);text-align:center;letter-spacing:.5px}
.lead{font-size:14px;line-height:24px;text-align:center;color:var(--text)}
.brand{font-family:"Montserrat",sans-serif;font-weight:700;color:var(--ink);letter-spacing:2px;display:flex;align-items:center;gap:10px}
.brand .dot{width:20px;height:20px;border-radius:50%;background:var(--pink)}
/* header */
.site-header{top:0;left:0;width:1200px;height:116px}
.site-header .brand{left:112px;top:62px;font-size:28px}
.call{right:112px;top:24px;font-family:"Montserrat",sans-serif;font-weight:600;font-size:19px;color:var(--ink);display:flex;align-items:center;gap:8px}
.call b{color:var(--red);font-weight:600}
.nav{right:112px;top:76px;display:flex;gap:40px;font-family:"Montserrat",sans-serif;font-size:14px;font-weight:600;color:#333}
/* hero */
.hero{top:116px;left:0;width:1200px;height:591px;overflow:hidden;
  background:radial-gradient(ellipse at 35% 55%,#c8265a 0%,rgba(200,38,90,0) 45%),radial-gradient(ellipse at 70% 40%,#6b449b 0%,rgba(107,68,155,0) 45%),linear-gradient(90deg,#b8123a 0%,#7a1d5e 45%,#1d2a7a 75%,#0355a3 100%)}
.hero-word{left:0;top:330px;width:1200px;text-align:center;font-family:"Montserrat",sans-serif;font-weight:700;font-size:104px;letter-spacing:10px;color:rgba(255,255,255,.18)}
.play{left:562px;top:270px;width:76px;height:76px;border-radius:50%;background:var(--white);display:flex;align-items:center;justify-content:center}
/* why */
.why-title{top:764px;left:0;width:1200px}
.why-lead{top:834px;left:240px;width:720px}
.feature{top:930px;width:210px}
.feature svg{display:block;height:80px}
.feature h3{margin-top:36px;font-size:17px;font-weight:600;color:var(--ink)}
.feature .rule{width:42px;height:3px;margin:12px 0 14px}
.feature p{font-size:13.5px;line-height:25px}
.btn{display:inline-block;margin-top:16px;height:38px;line-height:38px;padding:0 28px;border-radius:19px;color:var(--white);font-family:"Montserrat",sans-serif;font-size:12px;font-weight:700}
/* about */
.about{top:1394px;left:0;width:1200px;height:731px;background:var(--grey);overflow:hidden}
.stripe{top:0;width:28px;height:260px;background:#f3f3f3}
.about-copy{left:602px;top:140px;width:490px}
.about-copy h2{font-family:"Montserrat",sans-serif;font-weight:300;font-size:38px;color:var(--ink)}
.about-copy h4{margin-top:22px;font-family:"Montserrat",sans-serif;font-weight:600;font-size:19px;color:var(--red)}
.about-copy h4.blue{color:var(--blue);margin-top:42px}
.about-copy .strong{margin-top:10px;font-size:14px;font-weight:600;color:var(--ink);line-height:26px}
.about-copy ul{list-style:none;margin-top:14px;font-size:12.5px;line-height:27px;color:#333}
.about-copy .vision{margin-top:12px;font-size:13px;line-height:23px;color:#333}
/* projects */
.proj-title{top:2210px;left:0;width:1200px}
.proj-lead{top:2272px;left:240px;width:720px}
.card{width:470px;height:430px}
.card .panel{left:36px;top:177px;width:434px;height:260px;background:var(--grey)}
.card .photo{left:0;top:0;width:426px;height:298px}
.card h3{left:76px;top:326px;font-size:19px;font-weight:600;color:var(--ink)}
.card p{left:76px;top:364px;width:330px;font-size:13.5px;line-height:24px}
.view-all{left:534px;top:3331px;width:132px;height:46px;border-radius:23px;background:var(--sky);color:var(--white);font-family:"Montserrat",sans-serif;font-size:13px;font-weight:700;text-align:center;line-height:46px}
/* newsletter */
.newsletter{left:110px;top:3450px;width:980px;height:249px;border-radius:14px;background:linear-gradient(90deg,#ec1f27 0%,#e0203a 35%,#7a2a7e 70%,#0355a3 100%);overflow:hidden}
.newsletter .art{left:20px;top:20px;width:210px;height:210px;border-radius:10px;background:rgba(255,255,255,.14)}
.newsletter h2{left:249px;top:42px;font-family:"Montserrat",sans-serif;font-weight:600;font-size:38px;color:var(--white)}
.newsletter .sub{left:249px;top:101px;font-size:14px;font-style:italic;color:var(--white)}
.field{left:249px;top:141px;width:552px;height:52px;border-radius:26px 0 0 26px;background:var(--white);font-size:14px;color:#333;line-height:52px;padding-left:28px}
.signup{left:801px;top:141px;width:116px;height:52px;border-radius:0 26px 26px 0;background:var(--red);color:var(--white);font-family:"Montserrat",sans-serif;font-weight:700;font-size:15px;line-height:52px;text-align:center}
/* footer */
.foot-stripe{background:#f3f3f3;width:70px}
.footer-brand{left:110px;top:3760px;font-size:26px}
.social{right:110px;top:3752px;display:flex;gap:8px}
.social span{width:28px;height:28px;border-radius:50%}
.foot-rule{left:110px;width:980px;height:1px;background:#ddd}
.foot-col h5{font-size:15px;font-weight:600;color:var(--ink)}
.foot-col ul{list-style:none;margin-top:20px;font-size:12px;line-height:21px;color:#444}
.contact-row{display:flex;gap:18px;align-items:flex-start;margin-top:18px;font-size:12px;line-height:18px}
.copy{left:0;top:4104px;width:1200px;text-align:center;font-size:13px;color:#333}
</style>
</head>
<body>

<header class="site-header abs">
  <div class="brand abs"><span class="dot"></span>LUMIVANE</div>
  <div class="call abs">
    <svg width="18" height="18" viewBox="0 0 24 24"><path fill="#ec1f27" d="M6.6 10.8a15 15 0 0 0 6.6 6.6l2.2-2.2c.3-.3.7-.4 1-.2 1.1.4 2.3.6 3.6.6.6 0 1 .4 1 1V20c0 .6-.4 1-1 1A17 17 0 0 1 3 4c0-.6.4-1 1-1h3.5c.6 0 1 .4 1 1 0 1.3.2 2.5.6 3.6.1.3 0 .7-.2 1z"/></svg>
    CALL US:<b>555.204.7781</b>
  </div>
  <nav class="nav abs"><span>HOME</span><span>ABOUT</span><span>SERVICES</span><span>PROJECTS</span><span>NEWS</span><span>CONTACT</span></nav>
</header>

<section class="hero abs" role="img" aria-label="Video still: swirling red, pink and blue coloured smoke">
  <div class="hero-word abs">LUMIVANE</div>
  <div class="play abs"><svg width="30" height="30" viewBox="0 0 30 30"><path d="M8 4l18 11-18 11z" fill="#ec1f27"/></svg></div>
</section>

<h2 class="section-title why-title abs">WHY CHOOSE LUMIVANE</h2>
<p class="lead why-lead abs">Sed ut perspiciatis unde omnis iste natus error sit voluptatem accusantium doloremque laudantium, totam rem aperiam, eaque ipsa quae ab illo inventore veritatis et quasi architecto beatae vitae dicta sunt explicabo.</p>

<div class="feature abs" style="left:110px">
  <svg viewBox="0 0 80 80" width="80"><g fill="none" stroke="#0355a3" stroke-width="3"><path d="M4 76A72 72 0 0 1 76 4"/><path d="M16 76A60 60 0 0 1 76 16"/><path d="M28 76A48 48 0 0 1 76 28"/><path d="M40 76A36 36 0 0 1 76 40"/><path d="M52 76A24 24 0 0 1 76 52"/></g></svg>
  <h3>People on the spectrum</h3><div class="rule" style="background:var(--blue)"></div>
  <p>Sed ut perspiciatis unde omnis iste natuserror sit voluptlortm accusantium doloriatoru daloiu mtotam rem aperiam, eaquesa quae ab illo inventor.</p>
  <span class="btn" style="background:var(--navy)">READ MORE</span>
</div>
<div class="feature abs" style="left:372px">
  <svg viewBox="0 0 80 80" width="80"><g fill="none" stroke="#ec1f27" stroke-width="3" stroke-linejoin="round"><path d="M6 38l14-14 14 6 12-6 28 20-10 10"/><path d="M20 24L6 44l22 22 10-8"/><path d="M34 30l-10 12 6 6 12-10 14 14"/><path d="M40 64l6 6 6-6-6-6M48 56l6 6 6-6-6-6"/></g></svg>
  <h3>Partners</h3><div class="rule" style="background:var(--red)"></div>
  <p>Sed ut perspiciatis unde omnis iste natuserror sit voluptlortm accusantium doloriatoru daloiu mtotam rem aperiam, eaquesa quae ab illo inventor.</p>
  <span class="btn" style="background:var(--red)">READ MORE</span>
</div>
<div class="feature abs" style="left:632px">
  <svg viewBox="0 0 80 80" width="80"><g fill="none" stroke="#6b449b" stroke-width="3"><circle cx="24" cy="22" r="12"/><circle cx="56" cy="22" r="12"/><path d="M4 78V56a14 14 0 0 1 14-14h12a14 14 0 0 1 14 14v22"/><path d="M36 78V56a14 14 0 0 1 14-14h12a14 14 0 0 1 14 14v22"/></g></svg>
  <h3>Parents</h3><div class="rule" style="background:var(--purple)"></div>
  <p>Sed ut perspiciatis unde omnis iste natuserror sit voluptlortm accusantium doloriatoru daloiu mtotam rem aperiam, eaquesa quae ab illo inventor.</p>
  <span class="btn" style="background:var(--purple)">READ MORE</span>
</div>
<div class="feature abs" style="left:891px">
  <svg viewBox="0 0 80 80" width="80"><g fill="none" stroke="#e34298" stroke-width="3"><circle cx="40" cy="30" r="10"/><path d="M22 66V56a12 12 0 0 1 12-12h12a12 12 0 0 1 12 12v10"/><path d="M6 78h68"/><path d="M40 4l3 6 6 1-5 4 1 6-5-3-5 3 1-6-5-4 6-1z"/><path d="M14 18l2 4 4 1-3 3 1 4-4-2-4 2 1-4-3-3 4-1z"/><path d="M66 18l2 4 4 1-3 3 1 4-4-2-4 2 1-4-3-3 4-1z"/></g></svg>
  <h3>Customers</h3><div class="rule" style="background:var(--pink)"></div>
  <p>Sed ut perspiciatis unde omnis iste natuserror sit voluptlortm accusantium doloriatoru daloiu mtotam rem aperiam, eaquesa quae ab illo inventor.</p>
  <span class="btn" style="background:var(--pink)">READ MORE</span>
</div>

<section class="about abs">
  <div class="stripe abs" style="left:70px"></div><div class="stripe abs" style="left:130px"></div><div class="stripe abs" style="left:250px"></div><div class="stripe abs" style="left:330px"></div>
  <svg class="abs" style="left:0;top:0" width="600" height="731" viewBox="0 0 600 731">
    <defs>
      <linearGradient id="hexBrand" x1="0" y1="0" x2="1" y2="1"><stop offset="0" stop-color="#ec1f27"/><stop offset=".5" stop-color="#e34298"/><stop offset="1" stop-color="#0355a3"/></linearGradient>
      <linearGradient id="photoA" x1="0" y1="0" x2="1" y2="1"><stop offset="0" stop-color="#c7a98f"/><stop offset="1" stop-color="#8d8a8c"/></linearGradient>
      <linearGradient id="photoB" x1="0" y1="0" x2="1" y2="1"><stop offset="0" stop-color="#e8e4e2"/><stop offset="1" stop-color="#7d6a62"/></linearGradient>
    </defs>
    <polygon points="80,215 212,215 278,349 212,483 80,483 14,349" fill="url(#hexBrand)" opacity=".9" role="img" aria-label="Brand colour hexagon"/>
    <polygon points="250,96 470,96 580,286 470,476 250,476 140,286" fill="url(#photoA)" role="img" aria-label="Photo: a young woman and an older woman smiling together"/>
    <polygon points="200,372 364,372 442,510 364,649 200,649 124,510" fill="url(#photoB)" role="img" aria-label="Photo: a smiling young woman with glasses holding paper face cards"/>
  </svg>
  <div class="about-copy abs">
    <h2>ABOUT US</h2>
    <h4>MISSION STATEMENT</h4>
    <p class="strong">Lumivane aims to increase employment rate and give purpose of life to the maximum number of people on the spectrum though teleworking.</p>
    <ul>
      <li>Autism prevalence : ± 1 out of 100 persons</li>
      <li>Unemployment rate : ± 90% Fitting in a work environment is often difficult!</li>
      <li>Talent : good IQ but different brainwiring but leads to special talents</li>
      <li>Digital content production and teleworking / Freelancing are exponentially growing</li>
    </ul>
    <h4 class="blue">VISION</h4>
    <p class="vision">Like a hive, we provide a strong but lightweight structure, a connecting structure for partners with different roles to achieve our mission and common goals: to help as many people with ASD to do meaningful jobs.</p>
  </div>
</section>

<h2 class="section-title proj-title abs">PROJECTS</h2>
<p class="lead proj-lead abs">Sed ut perspiciatis unde omnis iste natus error sit voluptatem accusantium doloremque laudantium, totam rem aperiam, eaque ipsa quae ab illo inventore veritatis et quasi architecto beatae vitae dicta sunt explicabo.</p>

<article class="card abs" style="left:110px;top:2379px">
  <div class="panel abs"></div>
  <div class="photo abs" role="img" aria-label="Photo: a young couple working on a laptop at home" style="background:linear-gradient(135deg,#8a7a6c,#cfc4b8 55%,#6f6256)"></div>
  <h3 class="abs">Project Name</h3>
  <p class="abs">Sed ut perspiciatis unde omnis iste nat sit voluptatem accusantium doloremque laudantium, totam.</p>
</article>
<article class="card abs" style="left:621px;top:2379px">
  <div class="panel abs"></div>
  <div class="photo abs" role="img" aria-label="Photo with pink tint: two women talking on a sofa" style="background:linear-gradient(135deg,#b0368a,#e07ab8 55%,#8d2f7c)"></div>
  <h3 class="abs">Project Name</h3>
  <p class="abs">Sed ut perspiciatis unde omnis iste nat sit voluptatem accusantium doloremque laudantium, totam.</p>
</article>
<article class="card abs" style="left:110px;top:2851px">
  <div class="panel abs"></div>
  <div class="photo abs" role="img" aria-label="Photo with blue tint: two men reviewing documents together" style="background:linear-gradient(135deg,#0a4f9a,#3f86c8 55%,#0b3f7e)"></div>
  <h3 class="abs">Project Name</h3>
  <p class="abs">Sed ut perspiciatis unde omnis iste nat sit voluptatem accusantium doloremque laudantium, totam.</p>
</article>
<article class="card abs" style="left:621px;top:2851px">
  <div class="panel abs"></div>
  <div class="photo abs" role="img" aria-label="Photo: an older man and a young man using a laptop on a sofa" style="background:linear-gradient(135deg,#d9d6cf,#9a9288 55%,#e9e6e0)"></div>
  <h3 class="abs">Project Name</h3>
  <p class="abs">Sed ut perspiciatis unde omnis iste nat sit voluptatem accusantium doloremque laudantium, totam.</p>
</article>

<div class="view-all abs">VIEW ALL</div>

<div class="foot-stripe abs" style="left:0;top:3590px;height:548px"></div>
<div class="foot-stripe abs" style="left:290px;top:3770px;height:368px;width:70px"></div>

<section class="newsletter abs">
  <div class="art abs" role="img" aria-label="Decorative light panel"></div>
  <h2 class="abs">Sign up to our newsletter</h2>
  <p class="sub abs">Neque porro quisquam est qui dolorem ipsum quia dolor sit amet, consectetu</p>
  <div class="field abs">Email:</div>
  <div class="signup abs">SIGN UP</div>
</section>

<footer>
  <div class="brand footer-brand abs"><span class="dot"></span>LUMIVANE</div>
  <div class="social abs"><span style="background:var(--navy)"></span><span style="background:var(--sky)"></span><span style="background:var(--blue)"></span><span style="background:var(--red)"></span></div>
  <div class="foot-rule abs" style="top:3818px"></div>

  <div class="foot-col abs" style="left:110px;top:3845px;width:240px">
    <h5>Contact</h5>
    <div class="contact-row"><svg width="22" height="22" viewBox="0 0 24 24"><path d="M12 2a7 7 0 0 0-7 7c0 5 7 13 7 13s7-8 7-13a7 7 0 0 0-7-7z" fill="none" stroke="#ec1f27" stroke-width="1.8"/><circle cx="12" cy="9" r="2.5" fill="none" stroke="#ec1f27" stroke-width="1.8"/></svg><span>412 Harbor Lane,<br>Westfield Park</span></div>
    <div class="contact-row"><svg width="22" height="22" viewBox="0 0 24 24"><path fill="none" stroke="#0355a3" stroke-width="1.8" d="M6.6 10.8a15 15 0 0 0 6.6 6.6l2.2-2.2c.3-.3.7-.4 1-.2 1.1.4 2.3.6 3.6.6.6 0 1 .4 1 1V20c0 .6-.4 1-1 1A17 17 0 0 1 3 4c0-.6.4-1 1-1h3.5c.6 0 1 .4 1 1 0 1.3.2 2.5.6 3.6.1.3 0 .7-.2 1z"/></svg><span>8 800 555 0142<br>8 800 555 0187</span></div>
    <div class="contact-row"><svg width="22" height="22" viewBox="0 0 24 24"><rect x="2" y="5" width="20" height="14" rx="1" fill="none" stroke="#e34298" stroke-width="1.8"/><path d="M2 6l10 7 10-7" fill="none" stroke="#e34298" stroke-width="1.8"/></svg><span>hello@lumivane.test<br>team@lumivane.test</span></div>
  </div>
  <div class="foot-col abs" style="left:414px;top:3845px">
    <h5>Projects</h5>
    <ul><li>Lorem ipsum dolo</li><li>Consectetur adipiscing elit.</li><li>Fusce eget leo tincid</li><li>Donec consequat</li><li>Praesent elementum</li><li>Jmauris posuerat</li><li>Aenean a ex eu lectu</li></ul>
  </div>
  <div class="foot-col abs" style="left:662px;top:3845px">
    <h5>&nbsp;</h5>
    <ul><li>Lorem ipsum dolo</li><li>Consectetur adipiscing elit.</li><li>Fusce eget leo tincid</li><li>Donec consequat</li><li>Praesent elementum</li><li>Jmauris posuerat</li><li>Aenean a ex eu lectu</li></ul>
  </div>
  <div class="foot-col abs" style="left:925px;top:3845px">
    <h5>Other Links</h5>
    <ul><li>Lorem ipsum dolo</li><li>Consectetur adipiscing elit.</li><li>Fusce eget leo tincid</li><li>Donec consequat</li><li>Praesent elementum</li><li>Jmauris posuerat</li><li>Aenean a ex eu lectu</li></ul>
  </div>
  <div class="foot-rule abs" style="top:4071px"></div>
  <p class="copy abs">Copyright 2019 All Rights Reserved</p>
</footer>

</body>
</html>
```